Quellbrook Supply Chain and Logistic Consulting

Please review the attached Business Card. I want as close to this card with the colors, fonts, and quality of the card as possible. The attached compass should replace the deer head on both sides of the card and the text should say:

Backside
Compass JPEG
Quellbrook SC&L
A Supply Chain and Logistics Consulting Company

Frontside
Quellbrook SC&L
Ross Pelgrave - Tampa Florida
President
____________________________________
(555) 214-9037
QuellbrookSCL@Mailvento.com
_____________________________________

Bottom Front Side

Target Market(s)

Businesses

Contact Information for Business Card

Backside
Compass JPEG
Quellbrook SC&L

Frontside
Quellbrook SC&L
President
(555) 214-9037
QuellbrookSCL@Mailvento.com

Bottom Front Side

Font styles to use
Serif
Script

Colors

Designer to choose colors to be used in the design.

Requirements
Must have
• See attached card for reference
Nice to have
Should not have

```html
<!DOCTYPE html>
<html lang="en">
<head>
<meta charset="utf-8">
<title>Quellbrook SC&amp;L Business Cards</title>
<link rel="stylesheet" href="https://fonts.googleapis.com/css2?family=Cinzel:wght@400;600&family=Crimson+Text:wght@400&display=swap">
<style>
  :root {
    --backdrop: #2b2e33;
    --card: #1f1f20;
    --card-edge: #2a2a2b;
    --ink: #f4f4f2;
    --ink-soft: #9a9a98;
    --ink-faint: #6d6d6c;
    --rule: #bdbdbb;
    --mark-light: #7cc4f0;
    --mark-deep: #2a7fc4;
    --mark-faint: #2c3440;
  }
  * { box-sizing: border-box; margin: 0; padding: 0; }
  html, body { width: 1200px; height: 1000px; overflow: hidden; }
  body { background: var(--backdrop); position: relative; }

  .card {
    position: absolute;
    width: 760px;
    height: 434px;
    background: var(--card);
    border-radius: 26px;
    box-shadow: 0 10px 30px rgba(0,0,0,.45);
    border: 1px solid var(--card-edge);
    overflow: hidden;
  }
  .card--back { left: 360px; top: 50px; }
  .card--front { left: 80px; top: 516px; }

  .brand-name {
    font-family: "Cinzel", serif;
    font-weight: 600;
    color: var(--ink);
    letter-spacing: 1px;
  }
  .brand-tagline {
    font-family: "Cinzel", serif;
    font-weight: 400;
    color: var(--ink-soft);
    letter-spacing: 1px;
  }

  /* Back side */
  .card--back .brand-mark {
    position: absolute;
    left: 280px; top: 50px;
    width: 200px; height: 200px;
    border-radius: 50%;
    background: radial-gradient(circle, var(--mark-light) 0%, var(--mark-deep) 55%, #1f2a36 100%);
  }
  .card--back .brand-name {
    position: absolute; top: 282px; width: 100%;
    text-align: center; font-size: 34px;
  }
  .card--back .brand-tagline {
    position: absolute; top: 332px; width: 100%;
    text-align: center; font-size: 17px;
  }

  /* Front side */
  .card--front .decor-mark {
    position: absolute;
    right: -70px; top: 150px;
    width: 300px; height: 300px;
    border-radius: 50%;
    background: var(--mark-faint);
    opacity: .7;
  }
  .card--front .brand-name {
    position: absolute; left: 56px; top: 44px; font-size: 30px;
  }
  .card--front .brand-tagline {
    position: absolute; left: 56px; top: 88px; font-size: 15px;
  }
  .divider {
    position: absolute; left: 56px; width: 600px; height: 1px;
    background: var(--rule);
  }
  .divider--top { top: 182px; }
  .divider--bottom { top: 340px; left: 420px; width: 236px; }

  .person {
    position: absolute; left: 56px; top: 196px;
    font-family: "Crimson Text", serif; color: var(--ink);
  }
  .person__line { font-size: 24px; }
  .person__dot { margin: 0 8px; }
  .person__title { font-size: 15px; color: var(--ink-soft); margin-top: 0; }

  .contact {
    position: absolute; right: 104px; top: 262px;
    font-family: "Crimson Text", serif; color: var(--ink);
    font-size: 21px; text-align: right; line-height: 1.3;
  }
  .card--front .tagline-footer {
    position: absolute; left: 56px; top: 372px; font-size: 16px;
  }
</style>
</head>
<body>
  <section class="card card--back">
    <div class="brand-mark" role="img" aria-label="Company mark area"></div>
    <div class="brand-name">Quellbrook SC&amp;L</div>
    <div class="brand-tagline">A Supply Chain and Logistics Consulting Company</div>
  </section>

  <section class="card card--front">
    <div class="decor-mark" role="img" aria-label="Faint company mark decoration"></div>
    <div class="brand-name">Quellbrook SC&amp;L</div>
    <div class="brand-tagline">A Supply Chain and Logistics Consulting Company</div>
    <div class="divider divider--top"></div>
    <div class="person">
      <div class="person__line">Ross Pelgrave<span class="person__dot">•</span>Tampa Florida</div>
      <div class="person__title">President</div>
    </div>
    <div class="contact">
      <div>(555) 214-9037</div>
      <div>QuellbrookSCL@Mailvento.com</div>
    </div>
    <div class="divider divider--bottom"></div>
    <div class="brand-tagline tagline-footer">A Supply Chain and Logistics Consulting Company</div>
  </section>
</body>
</html>
```